Toward Bright Morrow (TWBM) Business Card - company with a mission

Note* The file attached... orange with "Toward Bright MORROW" (in CAPS) is our logo. I am also open to having the text "toward bright morrow" OUTSIDE the orange round logo for business card (so yes, you may take the text out).

The info: (the following info are separate. So either you can use Martin or Helena for now, but that will be 2 separate cards, not together in one card. Thanks!!

Martin K Pardo
202.555.0183
martin@towardbrightmorrow.example
Managing Partner

Helena R Voss
202.555.0147
helena@towardbrightmorrow.example
Managing Partner

Our website: www.towardbrightmorrow.example

TWBM LLC stands for Toward Bright Morrow (non profit arm is called dawn lift foundation)—our business is based out of New York City and has a non-profit arm where for every bar of soap you purchase, we donate a bar (don’t want any designs that limits us to only soap). Currently working with South Africa. We want the focus to be organic/natural soap with a mission.

Looking for a clean, fresh design.

Industry/Entity Type

Non-Profit

Requirements
Must have
• Clean, fresh, refreshing. Design should not be too busy.

```html
<!DOCTYPE html>
<html lang="en">
<head>
<meta charset="utf-8">
<title>Toward Bright Morrow — Business Card</title>
<link href="https://fonts.googleapis.com/css2?family=Urbanist:ital,wght@0,400;0,700;1,400&display=swap" rel="stylesheet">
<style>
  :root {
    --canvas: #ffffff;
    --charcoal: #3d3d3d;
    --apricot: #f6ae6b;
    --white: #ffffff;
    --ink: #3a3a3a;
  }
  * { margin: 0; padding: 0; box-sizing: border-box; }
  html, body {
    width: 1200px;
    height: 800px;
    overflow: hidden;
    background: var(--canvas);
    font-family: "Urbanist", "Century Gothic", sans-serif;
  }
  .card {
    position: absolute;
    left: 338px;
    width: 526px;
    height: 306px;
  }
  .card-front {
    top: 76px;
    background: var(--charcoal);
  }
  .card-back {
    top: 413px;
    background: var(--apricot);
  }
  .brand-disc {
    position: absolute;
    border-radius: 50%;
    display: flex;
    align-items: center;
    justify-content: center;
    color: var(--white);
    font-weight: 700;
  }
  .card-front .brand-disc {
    left: 167px;
    top: 45px;
    width: 192px;
    height: 192px;
    background: var(--apricot);
    box-shadow: 0 3px 10px rgba(0, 0, 0, 0.35);
    font-size: 52px;
    letter-spacing: 2px;
  }
  .tagline {
    position: absolute;
    left: 0;
    right: 0;
    top: 241px;
    text-align: center;
    color: var(--white);
    font-size: 21px;
    font-weight: 400;
  }
  .tagline strong { font-weight: 700; }
  .website {
    position: absolute;
    left: 20px;
    top: 22px;
    color: var(--white);
    font-style: italic;
    font-size: 17px;
  }
  .card-back .brand-disc {
    left: 400px;
    top: 27px;
    width: 100px;
    height: 100px;
    background: var(--charcoal);
    font-size: 27px;
    letter-spacing: 1px;
  }
  .contact {
    position: absolute;
    left: 20px;
    top: 195px;
    color: var(--white);
    font-size: 19px;
    line-height: 23px;
  }
  .contact .name {
    color: var(--ink);
    font-weight: 700;
    margin-bottom: 2px;
  }
</style>
</head>
<body>
  <section class="card card-front">
    <div class="brand-disc">TWBM</div>
    <p class="tagline">toward bright <strong>morrow</strong></p>
  </section>

  <section class="card card-back">
    <p class="website">www.towardbrightmorrow.example</p>
    <div class="brand-disc">TWBM</div>
    <div class="contact">
      <p class="name">Martin K Pardo</p>
      <p class="phone">202.555.0183</p>
      <p class="email">martin@towardbrightmorrow.example</p>
      <p class="role">Managing Partner</p>
    </div>
  </section>
</body>
</html>
```